Company or website name
- Quellmor, LLC
- Quellmor, LLC
- Quellmor, LLC is a research, science and technology based manufacturing company that formulates, develops, manufactures and packages a full complement of personal care products for domestic and international concerns. We private label and contract package personal care products, cosmetics, bath salts and powders and home fragrance products. Quellmor is conveniently located in Southern California adjacent to major transportation hubs and international airports. We utilize earth friendly, green manufacturing processes, maximize the use of renewable resource raw materials and minimize the use of non-renewable and petrochemical based raw materials. We provide formulation and product development services with low minimum order quantities and short lead times. Quellmor is the intersection between nature, science, beauty and innovation. We are a B-2-B company.
- We're looking for an ad design that can be used for both banner and column use online and in print. We manufacture bath and body products such as bath salts, body washes, body powders, bath oils and bubble baths, hair care products such as shampoos, conditioners and styling aids, skin care products such as anti-aging creams, cleansers, masks, toners and serums, color cosmetics such as eyeliners, mascaras, foundations and mineral make-up powders, manicure/pedicure products such as cuticle oils, sugar and salt scrubs and foot soaks/softeners and spa products such as seaweed wraps, cellulite creams, body masks, massage oils and candles. Our strengths are natural and organic product formulation, low minimums, competitive prices, complete research &development services new and innovative ingredients and fast turnaround times. Examples can be found at the following sites: http://www.zuvvo.com/ http://www.grovemantleboard.org/ http://www.trellisfinchjournal.com/ http://pondrixa.org/images/downloads/lumaletters/2009-10-lumaletter.pdf http://www.brindlewoxpress.com/

```html
<!DOCTYPE html>
<html lang="en">
<head>
<meta charset="utf-8">
<title>Quellmor Ad Set</title>
<link href="https://fonts.googleapis.com/css2?family=Crimson+Text:wght@400;600&display=swap" rel="stylesheet">
<style>
:root{
  --red:#c61f2e;
  --ink:#1e1e1e;
  --rule:#9a9a9a;
  --paper:#ffffff;
  --stage-top:#2b0f5c;
  --stage-mid:#0c0520;
  --stage-bottom:#000000;
  --hair-dark:#0d0d10;
  --hair-light:#6d7079;
  --brand:#b5552a;
}
*{box-sizing:border-box;margin:0;padding:0}
html,body{width:1200px;height:1043px;overflow:hidden}
body{
  position:relative;
  font-family:"Crimson Text",Georgia,serif;
  color:var(--ink);
  background:linear-gradient(180deg,var(--stage-top) 0%,var(--stage-mid) 40%,var(--stage-bottom) 58%);
}
.ad{position:absolute;background:var(--paper);display:flex;flex-direction:column;overflow:hidden}
.ad-photo{
  position:relative;flex:none;
  background:
    radial-gradient(ellipse at 70% 40%,rgba(210,170,160,.35),transparent 35%),
    linear-gradient(160deg,var(--hair-dark) 0%,var(--hair-light) 30%,var(--hair-dark) 55%,var(--hair-light) 80%,var(--hair-dark) 100%);
}
.brand-pill{
  position:absolute;left:0;top:var(--pill-top,8px);
  height:var(--pill-h);width:var(--pill-w);
  background:var(--paper);border-radius:0 999px 999px 0;
  display:flex;align-items:center;gap:calc(var(--pill-h)*.12);
  padding-left:calc(var(--pill-h)*.2);
}
.brand-dot{width:calc(var(--pill-h)*.32);height:calc(var(--pill-h)*.32);border-radius:50%;background:var(--brand);flex:none}
.brand-name{font-size:calc(var(--pill-h)*.5);color:var(--brand);font-weight:400;line-height:1}
.ad-body{flex:1;display:flex;flex-direction:column;align-items:center;justify-content:space-evenly;text-align:center;padding:0 var(--pad,10px)}
.headline{color:var(--red);font-size:var(--hs);line-height:1.2;font-weight:400}
.benefits{width:100%;border-top:1px solid var(--rule);border-bottom:1px solid var(--rule);padding:var(--bpad,6px) 0;font-size:var(--fs);line-height:1.5;text-transform:uppercase}
.category{background:var(--red);color:#fff;font-weight:600;font-size:var(--ls);padding:1px 8px;text-transform:uppercase;letter-spacing:.02em}
.products{width:var(--pw);height:var(--ph);background:linear-gradient(90deg,#f2c21f 0%,#f0d9c2 25%,#b9a6d6 45%,#9a6fc7 60%,#d7dce8 75%,#e4774a 100%);border-radius:6px 6px 3px 3px}
.product-list{font-size:var(--ps);text-transform:uppercase;line-height:1.4}
.ad-footer{flex:none;background:var(--red);color:#fff;text-align:center;font-size:var(--ffs);line-height:1.45;padding:var(--fpad,3px) 6px}

.ad-square{left:53px;top:184px;width:404px;height:403px;--hs:20px;--fs:10.5px;--ls:8.5px;--pw:70px;--ph:40px;--ps:9.5px;--ffs:8px;--fpad:2px;--pill-h:38px;--pill-w:120px;--pad:28px;--bpad:4px}
.ad-square .ad-photo{height:198px}
.ad-tall{left:481px;top:3px;width:434px;height:596px;--hs:27px;--fs:11.5px;--ls:13px;--pw:110px;--ph:78px;--ps:11.5px;--ffs:14px;--fpad:3px;--pill-h:42px;--pill-w:126px;--pad:24px;--bpad:6px}
.ad-tall .ad-photo{height:264px}
.ad-column{left:927px;top:3px;width:218px;height:597px;--hs:14.5px;--fs:8px;--ls:10px;--pw:100px;--ph:82px;--ps:12px;--ffs:11px;--fpad:8px;--pill-h:22px;--pill-w:62px;--pill-top:6px;--pad:10px;--bpad:4px}
.ad-column .ad-photo{height:166px}
.ad-banner{left:37px;top:608px;width:1113px;height:425px;flex-direction:row;background:transparent}
.ad-banner .ad-photo{width:650px;height:100%;--pill-h:55px;--pill-w:170px;--pill-top:12px}
.ad-banner .ad-panel{width:463px;height:100%;background:var(--paper);border-top:6px solid var(--red);display:flex;flex-direction:column;--hs:28px;--fs:14.5px;--ls:13.5px;--pw:165px;--ph:88px;--ps:13.5px;--ffs:15px;--fpad:6px;--pad:12px;--bpad:10px}
</style>
</head>
<body>

<section class="ad ad-square">
  <div class="ad-photo" role="img" aria-label="Profile of a woman with long glossy black hair">
    <div class="brand-pill"><span class="brand-dot"></span><span class="brand-name">Quellmor</span></div>
  </div>
  <div class="ad-body">
    <h2 class="headline">Creating Innovative Products<br>by Blending Science and Nature</h2>
    <p class="benefits">FDA Registered &nbsp;I&nbsp; Fast Turnaround &nbsp;I&nbsp; Low Minimums<br>Competitive Pricing &nbsp;I&nbsp; CGMP Quality Control</p>
    <span class="category">Hair Care Products</span>
    <div class="products" role="img" aria-label="Assorted hair care bottles and jars"></div>
    <p class="product-list">Shampoos &nbsp;I&nbsp; Conditioners &nbsp;I&nbsp; Pomades and Styling Products</p>
  </div>
  <footer class="ad-footer">4812 W. Larkspur Drive Suite 220, Fullerton, CA 92831, &nbsp;555.310.4401 P 555.310.4402 F info@quellmor.com</footer>
</section>

<section class="ad ad-tall">
  <div class="ad-photo" role="img" aria-label="Profile of a woman with long glossy black hair">
    <div class="brand-pill"><span class="brand-dot"></span><span class="brand-name">Quellmor</span></div>
  </div>
  <div class="ad-body">
    <h2 class="headline">Creating Innovative Products<br>by Blending Science and Nature</h2>
    <p class="benefits">FDA Registered &nbsp;I&nbsp; Fast Turnaround &nbsp;I&nbsp; Low Minimums<br>Competitive Pricing &nbsp;I&nbsp; CGMP Quality Control</p>
    <span class="category">Hair Care Products</span>
    <div class="products" role="img" aria-label="Assorted hair care bottles and jars"></div>
    <p class="product-list">Shampoos &nbsp;I&nbsp; Conditioners &nbsp;I&nbsp; Pomades and Styling Products</p>
  </div>
  <footer class="ad-footer">4812 W. Larkspur Drive Suite 220, Fullerton, CA 92831<br>555.310.4401 P 555.310.4402 F info@quellmor.com</footer>
</section>

<section class="ad ad-column">
  <div class="ad-photo" role="img" aria-label="Profile of a woman with long glossy black hair">
    <div class="brand-pill"><span class="brand-dot"></span><span class="brand-name">Quellmor</span></div>
  </div>
  <div class="ad-body">
    <h2 class="headline">Creating Innovative Products<br>by Blending Science and Nature</h2>
    <p class="benefits">FDA Registered &nbsp;I&nbsp; Fast Turnaround &nbsp;I&nbsp; Low Minimums<br>Competitive Pricing &nbsp;I&nbsp; CGMP Quality Control</p>
    <span class="category">Hair Care Products</span>
    <div class="products" role="img" aria-label="Assorted hair care bottles and jars"></div>
    <p class="product-list">Shampoos &nbsp;I&nbsp; Conditioners<br>I&nbsp; Pomades and Styling Products</p>
  </div>
  <footer class="ad-footer">4812 W. Larkspur Drive Suite 220,<br>Fullerton, CA 92831, 555.310.4401<br>P 555.310.4402 F info@quellmor.com</footer>
</section>

<section class="ad ad-banner">
  <div class="ad-photo" role="img" aria-label="Profile of a woman with long glossy black hair">
    <div class="brand-pill"><span class="brand-dot"></span><span class="brand-name">Quellmor</span></div>
  </div>
  <div class="ad-panel">
    <div class="ad-body">
      <h2 class="headline">Creating Innovative Products<br>by Blending Science and Nature</h2>
      <p class="benefits">FDA Registered &nbsp;I&nbsp; Fast Turnaround &nbsp;I&nbsp; Low Minimums<br>Competitive Pricing &nbsp;I&nbsp; CGMP Quality Control</p>
      <span class="category">Hair Care Products</span>
      <div class="products" role="img" aria-label="Assorted hair care bottles and jars"></div>
      <p class="product-list">Shampoos &nbsp;I&nbsp; Conditioners &nbsp;I&nbsp; Pomades and Styling Products</p>
    </div>
    <footer class="ad-footer">4812 W. Larkspur Drive Suite 220, Fullerton, CA 92831<br>555.310.4401 P 555.310.4402 F info@quellmor.com</footer>
  </div>
</section>

</body>
</html>
```